Marrowby Electric
Business Cards
Marrowby Electric -
Creative Brief
Modern
Peter Marrowby
Owner
17 Orvell St. Brookfield CT. 06804
pete@marrowbyelectric-example.com
www.marrowbyelectric-example.com
E-1 #374620

```html
<!DOCTYPE html>
<html lang="en">
<head>
<meta charset="utf-8">
<title>Marrowby Electric Stationery</title>
<link href="https://fonts.googleapis.com/css2?family=Montserrat:wght@400;600;700&display=swap" rel="stylesheet">
<style>
  :root{
    --bg:#3a3b3d;
    --paper:#ffffff;
    --navy:#0d3a66;
    --blue:#2f72b3;
    --sky:#7fb2de;
    --grey:#8a8d91;
    --ink:#1f2f44;
  }
  *{box-sizing:border-box;margin:0;padding:0}
  html,body{width:1200px;height:338px;overflow:hidden;background:var(--bg);font-family:'Montserrat',sans-serif}
  .stage{position:relative;width:1200px;height:338px}
  .sheet{position:absolute;background:var(--paper);overflow:hidden;box-shadow:0 2px 6px rgba(0,0,0,.45)}
  .sheet svg.swoosh{position:absolute;inset:0;width:100%;height:100%}
  .brand{position:absolute;display:flex;flex-direction:column;align-items:center;color:var(--navy);font-weight:700;text-transform:uppercase;line-height:1.05;text-align:center}
  .brand .mark{background:var(--navy);margin-bottom:3px}
  .brand .name{letter-spacing:.04em}
  .small{position:absolute;color:var(--ink);font-weight:400;line-height:1.35;white-space:nowrap}

  .card-front{left:34px;top:182px;width:104px;height:56px}
  .card-back{left:34px;top:250px;width:104px;height:56px}
  .letterhead-one{left:200px;top:20px;width:160px;height:300px}
  .letterhead-two{left:384px;top:20px;width:160px;height:300px}
  .envelope-window{left:624px;top:60px;width:204px;height:76px}
  .envelope-dl{left:624px;top:168px;width:204px;height:72px}
  .envelope-backs{position:absolute;left:893px;top:36px;width:170px;height:266px}
  .envelope-backs .env{position:absolute;left:0;width:170px;overflow:hidden;box-shadow:0 2px 6px rgba(0,0,0,.45)}
  .env-navy{top:0;height:80px;background:linear-gradient(180deg,var(--navy),var(--blue))}
  .env-grey{top:74px;height:74px;background:linear-gradient(180deg,#6d7075,#a9acb0)}
  .env-white{top:142px;height:124px;background:var(--paper)}
  .env svg{position:absolute;inset:0;width:100%;height:100%}
</style>
</head>
<body>
<div class="stage">

  <!-- Business card front -->
  <div class="sheet card-front">
    <svg class="swoosh" viewBox="0 0 104 56" preserveAspectRatio="none">
      <path d="M0 0 H104 V4 Q52 10 0 4 Z" fill="var(--blue)"/>
      <path d="M0 56 H104 V51 Q52 46 0 52 Z" fill="var(--navy)"/>
    </svg>
    <div class="brand" style="left:32px;top:14px;width:40px;font-size:4px">
      <span class="mark" style="width:7px;height:7px"></span>
      <span class="name">Marrowby Electric</span>
    </div>
  </div>

  <!-- Business card back -->
  <div class="sheet card-back">
    <svg class="swoosh" viewBox="0 0 104 56" preserveAspectRatio="none">
      <path d="M104 0 V56 H96 Q88 28 96 0 Z" fill="var(--navy)"/>
      <path d="M96 0 Q88 28 96 56 H92 Q84 28 92 0 Z" fill="var(--sky)"/>
    </svg>
    <div class="small" style="left:7px;top:8px;font-size:4px">
      <strong style="color:var(--navy);font-weight:700">Peter Marrowby</strong><br>Owner<br><br>
      17 Orvell St. Wrenholt CT. 06990<br>
      pete@marrowbyelectric-example.com<br>
      www.marrowbyelectric-example.com<br>
      Lic. No. 000-000
    </div>
  </div>

  <!-- Letterhead one -->
  <div class="sheet letterhead-one">
    <svg class="swoosh" viewBox="0 0 160 300" preserveAspectRatio="none">
      <path d="M0 0 H160 V6 Q80 14 0 6 Z" fill="var(--navy)"/>
      <path d="M160 0 V300 H152 Q140 150 154 0 Z" fill="var(--blue)"/>
      <path d="M0 300 H160 V292 Q80 284 0 294 Z" fill="var(--navy)"/>
    </svg>
    <div class="brand" style="left:50px;top:22px;width:60px;font-size:5px">
      <span class="mark" style="width:9px;height:9px"></span>
      <span class="name">Marrowby Electric</span>
    </div>
    <div class="small" style="left:14px;top:262px;font-size:3.4px">
      17 Orvell St. Wrenholt CT. 06990<br>
      pete@marrowbyelectric-example.com<br>
      www.marrowbyelectric-example.com
    </div>
  </div>

  <!-- Letterhead two -->
  <div class="sheet letterhead-two">
    <svg class="swoosh" viewBox="0 0 160 300" preserveAspectRatio="none">
      <path d="M0 0 H160 V8 Q80 2 0 12 Z" fill="var(--blue)"/>
      <path d="M0 0 V300 H8 Q20 150 6 0 Z" fill="var(--navy)"/>
      <path d="M0 300 H160 V290 Q80 298 0 288 Z" fill="var(--blue)"/>
    </svg>
    <div class="brand" style="left:50px;top:150px;width:60px;font-size:5px">
      <span class="mark" style="width:9px;height:9px"></span>
      <span class="name">Marrowby Electric</span>
    </div>
    <div class="small" style="left:30px;top:276px;width:100px;text-align:center;font-size:3.4px">
      17 Orvell St. Wrenholt CT. 06990 · www.marrowbyelectric-example.com
    </div>
  </div>

  <!-- Window envelope -->
  <div class="sheet envelope-window">
    <svg class="swoosh" viewBox="0 0 204 76" preserveAspectRatio="none">
      <path d="M0 0 H204 V5 Q102 12 0 4 Z" fill="var(--navy)"/>
      <path d="M204 0 V76 H196 Q186 38 198 0 Z" fill="var(--blue)"/>
    </svg>
    <div class="brand" style="left:70px;top:14px;width:60px;font-size:5px">
      <span class="mark" style="width:9px;height:9px"></span>
      <span class="name">Marrowby Electric</span>
    </div>
    <div class="small" style="left:74px;top:40px;font-size:3.4px">17 Orvell St. Wrenholt CT. 06990</div>
  </div>

  <!-- DL envelope -->
  <div class="sheet envelope-dl">
    <svg class="swoosh" viewBox="0 0 204 72" preserveAspectRatio="none">
      <path d="M0 72 H204 V66 Q102 58 0 66 Z" fill="var(--navy)"/>
      <path d="M0 0 V72 H6 Q14 36 4 0 Z" fill="var(--blue)"/>
    </svg>
    <div class="brand" style="left:10px;top:8px;width:50px;font-size:4.5px">
      <span class="mark" style="width:8px;height:8px"></span>
      <span class="name">Marrowby Electric</span>
    </div>
    <div class="small" style="left:12px;top:32px;font-size:3.4px">
      17 Orvell St. Wrenholt CT. 06990<br>www.marrowbyelectric-example.com
    </div>
  </div>

  <!-- Envelope backs -->
  <div class="envelope-backs">
    <div class="env env-navy">
      <svg viewBox="0 0 170 80" preserveAspectRatio="none">
        <path d="M0 0 L85 60 L170 0" fill="none" stroke="rgba(255,255,255,.35)" stroke-width="1"/>
      </svg>
    </div>
    <div class="env env-grey">
      <svg viewBox="0 0 170 74" preserveAspectRatio="none">
        <path d="M0 0 L85 52 L170 0" fill="none" stroke="rgba(255,255,255,.35)" stroke-width="1"/>
      </svg>
      <div class="brand" style="left:77px;top:28px;width:16px">
        <span class="mark" style="width:10px;height:10px;background:#ffffff"></span>
      </div>
    </div>
    <div class="env env-white">
      <svg viewBox="0 0 170 124" preserveAspectRatio="none">
        <path d="M0 0 L85 60 L170 0" fill="none" stroke="#d3d6da" stroke-width="1"/>
        <path d="M0 124 L70 70 M170 124 L100 70" fill="none" stroke="#e2e4e7" stroke-width="1"/>
      </svg>
      <div class="brand" style="left:55px;top:26px;width:60px;font-size:4.5px">
        <span class="mark" style="width:10px;height:10px"></span>
        <span class="name">Marrowby Electric</span>
      </div>
    </div>
  </div>

</div>
</body>
</html>
```